Website customization using WordPress Theme already purchased

Need informational website for Orla Brightwell LLC. Orla Brightwell is investment group company for multiple cloud based products and website. We need website for anyone coming to our website to be able get information on our products. I already have WordPress theme that I would like to use. Right person/company will be able to customize WordPress theme to our needs and be able to give us final product of 7-9 pages of complete website.

Industry/Entity Type

Investment

Number of Pages Required

5+ page

Colors
add136
3176b5
ec1f27
f37122

```html
<!DOCTYPE html>
<html lang="en">
<head>
<meta charset="utf-8">
<title>Orla Brightwell LLC</title>
<link rel="stylesheet" href="https://fonts.googleapis.com/css2?family=Open+Sans:ital,wght@0,400;0,600;0,700;1,400&display=swap">
<style>
:root{
  --green:#add136;
  --blue:#3176b5;
  --orange:#f37122;
  --red:#ec1f27;
  --ink:#555a5f;
  --text:#555;
  --partner:#6a6f75;
  --light:#f4f4f4;
  --line:#e3e3e3;
  --white:#fff;
}
*{box-sizing:border-box;margin:0;padding:0}
html,body{width:1200px;height:2326px;overflow:hidden}
body{position:relative;font-family:"Open Sans",Arial,sans-serif;color:var(--text);background:var(--white)}
a{color:inherit;text-decoration:none}

/* Hero */
.hero{position:absolute;left:0;top:0;width:1200px;height:650px;overflow:hidden}
.hero-photo{position:absolute;inset:0;background:
  radial-gradient(ellipse 420px 300px at 880px 330px,#7fa6d6 0%,rgba(90,130,190,.5) 45%,rgba(0,0,0,0) 80%),
  radial-gradient(ellipse 500px 420px at 420px 420px,#4f5f7c 0%,rgba(50,60,85,.4) 60%,rgba(0,0,0,0) 90%),
  linear-gradient(180deg,#1a1f2b 0%,#5b6a86 45%,#3c4a66 100%)}
.hero-shade{position:absolute;left:0;top:0;width:100%;height:120px;background:linear-gradient(180deg,rgba(0,0,0,.85),rgba(0,0,0,0))}
.brand{position:absolute;left:76px;top:32px;display:flex;align-items:center;gap:14px}
.brand-mark{width:52px;height:52px;border-radius:50%;background:var(--green)}
.brand-name{font-size:22px;font-weight:700;color:var(--white)}
.main-nav{position:absolute;right:74px;top:43px;display:flex;gap:4px}
.main-nav a{display:block;height:34px;line-height:34px;padding:0 18px;font-size:15px;font-weight:600;color:var(--white);border-radius:17px}
.main-nav a.active{background:var(--green);padding:0 25px}
.hero-title{position:absolute;left:74px;top:341px;width:602px;height:59px;background:rgba(255,255,255,.9);font-size:28px;font-weight:700;color:#222;line-height:59px;padding-left:20px;letter-spacing:.3px;white-space:nowrap}
.slider-dots{position:absolute;left:74px;top:581px;display:flex;gap:7px}
.slider-dots span{width:14px;height:14px;border-radius:50%;background:var(--white)}
.slider-dots span.on{background:var(--green)}

/* Services band */
.services{position:absolute;left:0;top:650px;width:1200px;height:393px;background:var(--blue);color:var(--white)}
.service{position:absolute;top:52px;width:320px;text-align:center}
.service-icon{width:90px;height:90px;border-radius:50%;background:var(--green);margin:0 auto;display:flex;align-items:center;justify-content:center}
.service h3{font-size:18px;font-weight:700;letter-spacing:.5px;margin-top:31px}
.service p{font-size:13.5px;line-height:23px;margin-top:13px;color:#e8f0f8}
.btn{display:inline-block;width:152px;height:40px;line-height:40px;border-radius:20px;background:var(--orange);color:var(--white);font-size:12px;font-weight:700;text-align:center;letter-spacing:.3px}
.service .btn{margin-top:26px}

/* Section headings */
.sec-title{position:absolute;font-size:23px;font-weight:700;color:var(--ink);letter-spacing:.2px}

/* Testimonial */
.quote-card{position:absolute;left:74px;top:1197px;width:513px;height:224px;border:1px solid var(--line);text-align:center}
.quote-card::after{content:"";position:absolute;left:246px;bottom:-11px;width:20px;height:20px;background:var(--white);border-right:1px solid var(--line);border-bottom:1px solid var(--line);transform:rotate(45deg)}
.avatar{position:absolute;left:280px;top:1147px;width:100px;height:100px;border-radius:50%;background:linear-gradient(160deg,#cfd6de,#6d7885);border:3px solid var(--white)}
.quote-name{margin-top:70px;font-size:18px;font-weight:600;color:var(--green)}
.quote-text{margin:12px auto 0;width:450px;font-size:13.5px;font-style:italic;line-height:26px;color:#555}
.pager{position:absolute;top:1454px;display:flex;gap:7px}
.pager span{width:12px;height:12px;border-radius:50%;background:#b7b7b7}
.pager span.on{background:var(--blue)}

/* News */
.news-card{position:absolute;left:614px;top:1145px;width:511px;height:320px;border:1px solid var(--line)}
.news-item{position:absolute;left:25px;display:flex;gap:25px}
.news-thumb{width:119px;height:89px;background:linear-gradient(135deg,#2c3e55,#8aa3c1)}
.news-thumb.alt{background:linear-gradient(135deg,#7ea8d8,#dfe9f5)}
.news-item p{width:320px;font-size:13.5px;line-height:25px;color:#555}
.news-item time{display:block;font-size:13px;font-weight:700;color:var(--orange);margin-top:2px}
.read-all{position:absolute;right:30px;bottom:18px;font-size:15px;font-weight:600;color:var(--green);letter-spacing:.5px}

/* Info columns */
.info{position:absolute;left:0;top:1511px;width:1200px;height:476px;background:var(--light)}
.col{position:absolute;top:44px;width:331px}
.col h2{font-size:22px;font-weight:700;color:var(--ink);white-space:nowrap;letter-spacing:-.2px;line-height:30px}
.col-photo{margin-top:20px;width:331px;height:159px}
.col p{margin-top:20px;font-size:13.5px;line-height:25px;color:#555}
.col .btn{margin-top:18px}

/* Partners */
.partners{position:absolute;left:74px;top:2040px;width:1052px;height:50px;display:flex;justify-content:space-between;align-items:center}
.partner{display:flex;align-items:center;gap:10px;font-size:24px;font-weight:600;color:var(--partner)}
.partner i{display:block;width:22px;height:22px;background:var(--partner)}

/* Footer */
.footer{position:absolute;left:0;top:2150px;width:1200px;height:176px;background:var(--blue);color:var(--white)}
.foot-nav{position:absolute;left:76px;top:32px;display:flex;gap:35px;font-size:15px;font-weight:600}
.foot-brand{position:absolute;left:76px;top:80px;display:flex;align-items:center;gap:10px}
.foot-brand .brand-mark{width:34px;height:34px}
.foot-brand span{font-size:16px;font-weight:700}
.copyright{position:absolute;left:76px;top:124px;font-size:12px}
.follow{position:absolute;left:946px;top:32px;font-size:16px;font-weight:600}
.social{position:absolute;left:946px;top:72px;display:flex;gap:17px}
.social span{width:20px;height:20px;border-radius:3px;background:var(--white)}
</style>
</head>
<body>

<header class="hero">
  <div class="hero-photo" role="img" aria-label="Photo of a hand touching a hexagon grid of cloud service labels over a blue blurred background"></div>
  <div class="hero-shade"></div>
  <a class="brand" href="#"><span class="brand-mark"></span><span class="brand-name">Orla Brightwell</span></a>
  <nav class="main-nav">
    <a class="active" href="#">Home</a><a href="#">About Us</a><a href="#">Services</a><a href="#">Blog</a><a href="#">Clients</a><a href="#">News</a><a href="#">Contact Us</a>
  </nav>
  <h1 class="hero-title">WE ARE IN CLOUD SERVICES COMPANY</h1>
  <div class="slider-dots"><span class="on"></span><span></span><span></span><span></span></div>
</header>

<section class="services">
  <div class="service" style="left:80px">
    <div class="service-icon">
      <svg width="36" height="40" viewBox="0 0 36 40" fill="none" stroke="#fff" stroke-width="3" stroke-linecap="round"><path d="M11 26c-4-3-6-7-6-11a13 13 0 0 1 26 0c0 4-2 8-6 11v4H11z"/><path d="M13 35h10M15 39h6"/></svg>
    </div>
    <h3>IT SERVICES</h3>
    <p>Vestibulum ante ipsum primis in faucibus orci<br>luctus et ultrices posuere cubilia Curaeq<br>uisque sed tortor a est</p>
    <a class="btn" href="#">READ MORE</a>
  </div>
  <div class="service" style="left:440px">
    <div class="service-icon">
      <svg width="46" height="32" viewBox="0 0 46 32"><path fill="#fff" d="M12 31a11 11 0 0 1-2-21.8A14 14 0 0 1 36 10a10.5 10.5 0 0 1-1 21z"/></svg>
    </div>
    <h3>CLOUD SERVICES</h3>
    <p>Vestibulum ante ipsum primis in faucibus orci<br>luctus et ultrices posuere cubilia Curaeq<br>uisque sed tortor a est</p>
    <a class="btn" href="#">READ MORE</a>
  </div>
  <div class="service" style="left:798px">
    <div class="service-icon">
      <svg width="46" height="38" viewBox="0 0 46 38" fill="#fff"><ellipse cx="19" cy="15" rx="18" ry="13"/><path d="M8 24l-4 9 11-6z"/><ellipse cx="30" cy="22" rx="14" ry="10" stroke="#add136" stroke-width="3"/><path d="M38 29l5 7-10-4z"/></svg>
    </div>
    <h3>IT SUPPORT</h3>
    <p>Vestibulum ante ipsum primis in faucibus orci<br>luctus et ultrices posuere cubilia Curaeq<br>uisque sed tortor a est</p>
    <a class="btn" href="#">READ MORE</a>
  </div>
</section>

<h2 class="sec-title" style="left:74px;top:1090px">WHAT OUR CLIENTS SAYS</h2>
<div class="quote-card">
  <p class="quote-name">Name Heading</p>
  <p class="quote-text">“ Nunc a dui id turpis convallis semper. Nunc dignissim lectus vitae eros placerat euismod. Aenean lacinia sodales eros, sit amet molestie enim consectetur eget adipiscing eu sit amet turpis....”</p>
</div>
<div class="avatar" role="img" aria-label="Client portrait"></div>
<div class="pager" style="left:305px"><span class="on"></span><span></span><span></span></div>

<h2 class="sec-title" style="left:612px;top:1090px">RECENT NEWS</h2>
<div class="news-card">
  <article class="news-item" style="top:30px">
    <div class="news-thumb" role="img" aria-label="News photo of server hardware"></div>
    <div><p>Nunc a dui id turpis convallis semper. Nunc dignissim lectus vitae eros placerat euismod. Aenean lacinia sodales eros, sit amet molestie</p><time>NOV 02, 2016</time></div>
  </article>
  <article class="news-item" style="top:152px">
    <div class="news-thumb alt" role="img" aria-label="News photo of cloud technology concept"></div>
    <div><p>Nunc a dui id turpis convallis semper. Nunc dignissim lectus vitae eros placerat euismod. Aenean lacinia sodales eros, sit amet molestie</p><time>NOV 02, 2016</time></div>
  </article>
  <a class="read-all" href="#">READ ALL NEWS</a>
</div>

<section class="info">
  <div class="col" style="left:74px">
    <h2>ABOUT ORLA BRIGHTWELL LLC</h2>
    <div class="col-photo" role="img" aria-label="Photo of a laptop on a wooden desk" style="background:linear-gradient(135deg,#6b4a2a,#d2a466 55%,#3a2a1c)"></div>
    <p>Nunc a dui id turpis convallis semper. Nunc dignissim lectus vitae eros placerat euismod. Aenean lacinia sodales eros, sit amet molestie enim consectetur eget.</p>
    <a class="btn" href="#">READ MORE</a>
  </div>
  <div class="col" style="left:434px">
    <h2>OUR TEAM</h2>
    <div class="col-photo" role="img" aria-label="Photo of a smiling business team" style="background:linear-gradient(135deg,#e9eef3,#9aa7b6 55%,#4b5a6e)"></div>
    <p>Nunc a dui id turpis convallis semper. Nunc dignissim lectus vitae eros placerat euismod. Aenean lacinia sodales eros, sit amet molestie enim consectetur eget.</p>
    <a class="btn" href="#">READ MORE</a>
  </div>
  <div class="col" style="left:792px">
    <h2>CAREER WITH US</h2>
    <div class="col-photo" role="img" aria-label="Photo of colleagues planning on a glass board" style="background:linear-gradient(135deg,#cfe0dc,#9fb9c4 50%,#506070)"></div>
    <p>Nunc a dui id turpis convallis semper. Nunc dignissim lectus vitae eros placerat euismod. Aenean lacinia sodales eros, sit amet molestie enim consectetur eget.</p>
    <a class="btn" href="#">READ MORE</a>
  </div>
</section>

<div class="partners">
  <span class="partner"><i></i>Quillon</span>
  <span class="partner"><i></i>Tessmar</span>
  <span class="partner"><i></i>Brantwick Group</span>
  <span class="partner"><i></i>Loderan</span>
  <span class="partner"><i></i>Vexhollow</span>
</div>

<footer class="footer">
  <nav class="foot-nav">
    <a href="#">Home</a><a href="#">About Us</a><a href="#">Services</a><a href="#">Blog</a><a href="#">Clients</a><a href="#">News</a><a href="#">Contact Us</a>
  </nav>
  <div class="foot-brand"><span class="brand-mark"></span><span>Orla Brightwell</span></div>
  <p class="copyright">Copyright © 2016. Company Name All Right Reserved</p>
  <p class="follow">Follow Us</p>
  <div class="social" aria-label="Social links"><span></span><span></span><span></span><span></span><span></span></div>
</footer>

</body>
</html>
```